WordPress WEB DESIGN & CODING for www.quelbrix-aerial.com Wireless Tower Contruction

WEB DESIGN & CODING for www.quelbrix-aerial.com
Wireless Tower Contruction Industry

SLOGAN: SERVICE AT A HIGHER LEVEL

Brannock Spires LLC has been in business since 2014 with combined professional Team experience of over 40 years.

Our Team is composed of long-time industry professionals in every aspect of the wireless telecommunications and commercial construction industries, including project management and site acquisition.

Brannock Spires specializes in providing tower installation services for the Wireless Telecommunications in the Southeastern of the United States.

Our key services are Wireless Tower Construction, Installation & Maintenance

Site audits and Tower mapping
Mount swaps and Modifications
Hardline & Jumper Installation
Antenna & Radio Install, Decom, Testing and Maintenance
Tower Lighting Installation & Testing
Fiber / Sweep / RET/ PIM Testing
Small Cells
Civil installation (concrete/steel platforms/electrical)
____________________________________________________________________

we need a clean yet vibrant, energetic website design that will convey our tower installation work to the fullest... It should use the navy and green colors of our logo and it must be mobile friendly and coded for both Android & IOS;
the site structure:
HOME
ABOUT
SERVICES
CONTRACT
CAREERS
GALLERY

I also attach a few pics we bought on shutterstock so these can be used if needed as we own them...

Target Market(s)

Client: large companies looking for general contractor or installation contractor in the market

Industry/Entity Type

Wireless Communication

Coding

Coded - Design and coding required

Number of Pages Required

4 page

Font styles to use
Sans Serif

Colors
0555a3
00a990
ffffff

Requirements
Must have
• Wordpress - must be both desktop mobile friendly and mobile is the key -
• should open swiftly on both Android & iOS
• See power point file with presentation about the company; page 5 is our keyservices but other contents can be used too
Nice to have
• panorama pics changing from the height/tower view showing the full overview, could be a slideshow or a short video...
Should not have
• flash animation does not work on iOS so this should be avoided.

```html
<!DOCTYPE html>
<html lang="en">
<head>
<meta charset="utf-8">
<title>Brannock Spires LLC — Service At A Higher Level</title>
<link href="https://fonts.googleapis.com/css2?family=Open+Sans:wght@400;600;700;800&family=Playfair+Display:wght@700&display=swap" rel="stylesheet">
<style>
:root{
  --navy:#0555a3;
  --green:#00a990;
  --white:#ffffff;
  --ink:#222a33;
  --muted:#4a4f55;
  --line:#e6e9ee;
}
*{box-sizing:border-box;margin:0;padding:0}
html,body{width:1200px;height:3904px;overflow:hidden}
body{position:relative;font-family:"Open Sans",Arial,sans-serif;color:var(--ink);background:var(--white)}
.abs{position:absolute}
.serif{font-family:"Playfair Display",Georgia,serif;font-weight:700}

/* top bar */
.topbar{left:0;top:0;width:1200px;height:27px;background:var(--green);color:var(--white);font-size:9px}
.topbar .info{position:absolute;top:8px;display:flex;align-items:center;gap:6px;white-space:nowrap}
.topbar .dots{position:absolute;left:868px;top:5px;display:flex;gap:5px}
.topbar .dots span{width:16px;height:16px;border-radius:50%;background:var(--white);display:block}

/* hero */
.hero{left:0;top:27px;width:1200px;height:463px;background:linear-gradient(90deg,#bfc2c6 0%,#eeeff0 22%,#fafafa 50%,#eeeff0 78%,#bcbfc3 100%)}
.brand{font-weight:700;color:var(--navy);font-size:26px;line-height:1;letter-spacing:-.3px}
.nav{left:655px;top:76px;display:flex;gap:17px;font-size:11px;color:#333}
.nav .active{font-weight:700;color:#111}
.btn{background:var(--navy);color:var(--white);font-size:11px;font-weight:700;display:flex;align-items:center;justify-content:center}

/* about */
.about-bg{left:0;top:490px}
.about h2{left:0;width:1200px;top:518px;text-align:center;font-size:30px;color:var(--white);letter-spacing:.5px}
.about .lead{left:250px;top:586px;width:330px;font-size:12.5px;line-height:20px;color:var(--white)}
.about .over{left:250px;top:642px;font-size:15.5px;font-weight:700;color:var(--white)}
.about .years{left:248px;top:665px;font-size:55px;font-weight:800;color:var(--white);letter-spacing:.5px}
.about .body{left:250px;width:335px;font-size:9.8px;line-height:17px;color:#e8eef7}
.photo{display:block}

/* services */
.services h2{left:0;width:1200px;top:1022px;text-align:center;font-size:30px;color:var(--navy)}
.services .sub{left:0;width:1200px;top:1068px;text-align:center;font-size:14px;font-weight:600;letter-spacing:1.3px;color:#1b1f24}
.card{width:218px;height:223px;background:var(--white);box-shadow:0 2px 10px rgba(0,0,0,.09);padding:30px 4px 0 20px}
.card.featured{border:3px solid var(--green);box-shadow:none;padding:27px 1px 0 17px}
.card .icon{width:62px;height:62px;border:2px solid var(--green);border-radius:6px;background:#e8f7f4}
.card h3{font-size:10.5px;font-weight:700;color:#1b1f24;margin-top:28px;line-height:14px;white-space:nowrap}
.card p{font-size:9.6px;line-height:14px;color:#333;margin-top:5px;width:182px}
.card .more{font-size:9.6px;font-weight:700;color:var(--green);margin-top:6px;display:block}

/* turnkey */
.panel-title{font-size:30px;color:var(--white)}
.panel-sub{font-size:14.5px;color:var(--white)}
.ticks{list-style:none;color:var(--white);font-size:9px}
.ticks li{position:relative;padding-left:13px;line-height:15px;white-space:nowrap}
.ticks li::before{content:"\2605";position:absolute;left:0;top:0;font-size:8px}

/* gallery */
.gallery h2{left:0;width:1200px;top:2416px;text-align:center;font-size:30px;color:var(--navy)}

/* wireless */
.wireless h2{left:250px;top:3066px;font-size:30px;color:var(--navy)}
.wireless .sub{left:250px;top:3106px;font-size:14.5px;color:#1b1f24;font-weight:600}
.wireless .intro{left:250px;top:3136px;width:350px;font-size:9.3px;line-height:14px;color:#333}
.dark-ticks{list-style:none;font-size:9.8px;color:#222}
.dark-ticks li{position:relative;padding-left:13px;height:21px;line-height:14px;white-space:nowrap}
.dark-ticks li::before{content:"\2605";position:absolute;left:0;top:0;font-size:8px}

/* footer */
.footer{left:0;top:3446px;width:1200px;height:458px;background:linear-gradient(180deg,#0a58a5,#0451a0)}
.sub-title{left:526px;top:3494px;font-size:28px;color:var(--white)}
.sub-lead{left:526px;top:3530px;font-size:14.5px;color:var(--white);letter-spacing:.3px}
.input{left:526px;top:3566px;width:310px;height:35px;border:1px solid #b9cde4;color:var(--white);font-size:9px;padding:12px 16px}
.hr{height:1px;background:rgba(255,255,255,.35)}
.social{width:27px;height:27px;border-radius:50%;background:#0b3f7a}
.quick{list-style:none}
.quick li{font-size:9px;color:#dbe6f3;height:20px}
</style>
</head>
<body>

<!-- top bar -->
<div class="abs topbar">
  <div class="info" style="left:250px">
    <svg width="9" height="12" viewBox="0 0 9 12"><path d="M4.5 0A4.5 4.5 0 0 0 0 4.5C0 8 4.5 12 4.5 12S9 8 9 4.5A4.5 4.5 0 0 0 4.5 0Zm0 6.3a1.8 1.8 0 1 1 0-3.6 1.8 1.8 0 0 1 0 3.6Z" fill="#fff"/></svg>
    <span>Address : Pell Row Arden 48210, KR Q7M</span>
  </div>
  <div class="info" style="left:468px">
    <svg width="11" height="8" viewBox="0 0 11 8"><rect width="11" height="8" rx="1" fill="#fff"/><path d="M0.5 0.8 5.5 4.6 10.5 0.8" stroke="#00a990" fill="none"/></svg>
    <span>Phone Number : 555 018 274</span>
  </div>
  <div class="info" style="left:628px">
    <svg width="10" height="10" viewBox="0 0 10 10"><path d="M2 0.5 3.6 2.4 2.8 3.8C3.5 5.3 4.7 6.5 6.2 7.2L7.6 6.4 9.5 8 8.6 9.5C4.4 9.3 0.7 5.6 0.5 1.4Z" fill="#fff"/></svg>
    <span>Email : info@brannockspires.com</span>
  </div>
  <div class="dots" aria-label="Social links"><span></span><span></span><span></span><span></span></div>
</div>

<!-- hero -->
<section class="abs hero" role="img" aria-label="Black and white photo of lattice telecom towers with antennas against a pale sky"></section>
<div class="abs brand" style="left:250px;top:52px">Brannock Spires</div>
<nav class="abs nav"><span class="active">Home</span><span>About</span><span>Services</span><span>Contract</span><span>Careers</span><span>Gallery</span></nav>
<h1 class="abs serif" style="left:0;width:1200px;top:188px;text-align:center;font-size:40px;color:#1b1f24"><em style="font-style:normal;color:var(--navy)">Service At A</em> Higher Level</h1>
<p class="abs" style="left:0;width:1200px;top:245px;text-align:center;font-size:18px;line-height:25px;color:#222">Brannock Spires LLC has been in business since 2014 with combined<br>professional Team experience of over 40 years.</p>
<div class="abs btn" style="left:553px;top:311px;width:94px;height:31px">Read More</div>

<!-- about -->
<svg class="abs about-bg" width="1200" height="540" viewBox="0 0 1200 540"><polygon points="0,0 1200,0 1200,537 600,442 0,537" fill="#0555a3"/></svg>
<div class="about">
  <h2 class="abs serif">About The Company</h2>
  <p class="abs lead">Brannock Spires LLC has been in business since <b>2014</b> with combined professional Team</p>
  <div class="abs over">EXPERIENCE OF OVER</div>
  <div class="abs years">40 YEARS</div>
  <p class="abs body" style="top:740px">Our Team is composed of long-time industry professionals in every aspect of the wireless telecommunications and commercial construction industries, including project management and site acquisition.</p>
  <p class="abs body" style="top:802px">Brannock Spires specializes in providing turn-key service by integrating services for the Wireless Telecommunications and Commercial Construction industries, maintaining a footprint throughout the South Eastern, Central and Midwest regions of the United States.</p>
  <div class="abs photo" style="left:603px;top:589px;width:212px;height:267px;background:linear-gradient(160deg,#6aa4dc,#2f6fb5 60%,#1d5aa2)" role="img" aria-label="Blue-toned photo of a lattice tower against the sky"></div>
  <div class="abs photo" style="left:723px;top:624px;width:228px;height:291px;background:radial-gradient(circle at 55% 45%,#f4e4c2 0%,#d3b184 35%,#7a5d3e 75%,#2a2018 100%)" role="img" aria-label="Photo looking up through a steel tower toward the sun"></div>
</div>

<!-- services -->
<section class="services">
  <h2 class="abs serif">Our key Services</h2>
  <div class="abs sub">Are Wireless Tower Construction,Installation &amp; Maintenance</div>

  <div class="abs card" style="left:250px;top:1121px">
    <div class="icon" role="img" aria-label="Icon of a radio tower"></div>
    <h3>Site Audits and Tower Mapping</h3>
    <p>Lorem Ipsum is simply dummy text of the printing and typesetting industry. Lorem Ipsum has been</p>
    <span class="more">Read More</span>
  </div>
  <div class="abs card featured" style="left:492px;top:1121px">
    <div class="icon" role="img" aria-label="Icon of a mount and gauge"></div>
    <h3>Mount swaps and Modifications</h3>
    <p>Lorem Ipsum is simply dummy text of the printing and typesetting industry. Lorem Ipsum has been</p>
    <span class="more">Read More</span>
  </div>
  <div class="abs card" style="left:733px;top:1121px">
    <div class="icon" role="img" aria-label="Icon of equipment with a gear"></div>
    <h3>Hardline &amp; Jumper Installation</h3>
    <p>Lorem Ipsum is simply dummy text of the printing and typesetting industry. Lorem Ipsum has been</p>
    <span class="more">Read More</span>
  </div>
  <div class="abs card" style="left:250px;top:1368px">
    <div class="icon" role="img" aria-label="Icon of two antenna masts"></div>
    <h3>Antenna &amp; Radio Install, Decom,<br>Testing and Maintenance</h3>
    <p>Lorem Ipsum is simply dummy text of the printing and typesetting</p>
    <span class="more">Read More</span>
  </div>
  <div class="abs card" style="left:492px;top:1368px">
    <div class="icon" role="img" aria-label="Icon of a lit beacon tower"></div>
    <h3>Tower Lighting Installation &amp; Testing</h3>
    <p>Lorem Ipsum is simply dummy text of the printing and typesetting industry. Lorem Ipsum has been</p>
    <span class="more">Read More</span>
  </div>
  <div class="abs card" style="left:733px;top:1368px">
    <div class="icon" role="img" aria-label="Icon of fiber optic cable"></div>
    <h3>Fiber / Sweep / RET/ PIM Testing</h3>
    <p>Lorem Ipsum is simply dummy text of the printing and typesetting industry. Lorem Ipsum has been</p>
    <span class="more">Read More</span>
  </div>
</section>

<!-- full turn key -->
<section class="turnkey">
  <div class="abs" style="left:0;top:1651px;width:600px;height:452px;background:linear-gradient(120deg,#2bbd9f,#00a990)"></div>
  <div class="abs" style="left:600px;top:1651px;width:600px;height:452px;background:linear-gradient(180deg,#4a4f6e 0%,#7a6f82 45%,#c98b6e 80%,#e0a07a 100%)" role="img" aria-label="Photo of a cell tower with antennas at sunset"></div>
  <h2 class="abs serif panel-title" style="left:250px;top:1702px">Full Turn Key Services</h2>
  <div class="abs panel-sub" style="left:250px;top:1747px">Execution – From Scip To On-air</div>
  <ul class="abs ticks" style="left:250px;top:1786px;width:340px">
    <li style="height:33px">Brannock Spires LLC has a long track record of quality, professionalism,</li>
    <li style="height:33px">accountability and safety in wireless tower construction.</li>
    <li style="height:33px">Site Acquisition / Leasing / Regulatory / Zoning &amp; Permitting</li>
    <li style="height:33px">Engineering and Design (CD's, SA)</li>
    <li style="height:33px">Project Scoping</li>
    <li style="height:33px">Project Logistics Support</li>
    <li style="height:33px">Construction Management / Quality Control / Safety</li>
  </ul>

  <div class="abs" style="left:250px;top:2047px;width:350px;height:339px;background:linear-gradient(160deg,#dfe8f1,#9db6cf 55%,#5f86ad)" role="img" aria-label="Photo of a cell tower with antenna panels under a cloudy sky"></div>
  <div class="abs" style="left:600px;top:2047px;width:351px;height:339px;background:var(--navy)"></div>
  <h2 class="abs serif panel-title" style="left:638px;top:2095px">Full Turn Key</h2>
  <div class="abs panel-sub" style="left:638px;top:2140px">Project Management</div>
  <ul class="abs ticks" style="left:638px;top:2176px;width:300px">
    <li style="height:33px">New Site Builds and Carrier Additions on Tower Structures,</li>
    <li style="height:43px">Rooftops, Watertanks, Stealthpoles and other<br>Telecommunication Sites</li>
    <li style="height:33px">Telecommunication Site Modifications/Design</li>
    <li style="height:33px">Wireline Construction &amp; Management/Design</li>
    <li style="height:33px">Full In-House Training for Tower/Civil Safety Plans</li>
  </ul>
</section>

<!-- gallery -->
<section class="gallery">
  <h2 class="abs serif">Gallery</h2>
  <div class="abs" style="left:0;top:2489px;width:300px;height:480px;background:linear-gradient(180deg,#3d5f8c,#8fa6bf 55%,#5b6b80)" role="img" aria-label="Photo of a tall lattice tower and clouds"></div>
  <div class="abs" style="left:300px;top:2489px;width:300px;height:241px;background:linear-gradient(180deg,#d9d9d9,#a9a9a9)" role="img" aria-label="Black and white photo of several towers"></div>
  <div class="abs" style="left:600px;top:2489px;width:300px;height:241px;background:radial-gradient(circle at 50% 60%,#f2dcb0,#b58d5e 50%,#2e251c)" role="img" aria-label="Photo looking up a tower toward the sun"></div>
  <div class="abs" style="left:900px;top:2489px;width:300px;height:241px;background:linear-gradient(180deg,#3d5680,#8a9ab3 60%,#c7ccd4)" role="img" aria-label="Photo of a tower over a snowy town"></div>
  <div class="abs" style="left:300px;top:2730px;width:320px;height:239px;background:linear-gradient(135deg,#6b4a3a,#d8553f 45%,#c8c2b8)" role="img" aria-label="Photo of a worker's red hard hat in front of steel structure"></div>
  <div class="abs" style="left:620px;top:2730px;width:280px;height:239px;background:linear-gradient(160deg,#2f5d99,#5a86bd 60%,#a9c0db)" role="img" aria-label="Photo of steel tower beams against blue sky"></div>
  <div class="abs" style="left:900px;top:2730px;width:300px;height:239px;background:linear-gradient(180deg,#b7b7b7,#6d6d6d)" role="img" aria-label="Black and white photo looking up inside a tower"></div>
</section>

<!-- wireless tower -->
<section class="wireless">
  <h2 class="abs serif">Wireless Tower</h2>
  <div class="abs sub">Construction</div>
  <p class="abs intro">Brannock Spires crews and tiger teams are trained on the latest technologies, with experience in all facets of wireless telecom work:</p>
  <ul class="abs dark-ticks" style="left:250px;top:3178px;width:350px">
    <li>Site audits and Tower mapping</li>
    <li>Mount swaps and Modifications</li>
    <li>Hardline &amp; Jumper Installation</li>
    <li>Antenna &amp; Radio Install, Decom, Testing and Maintenance</li>
    <li>Tower Lighting Installation &amp; Testing</li>
    <li>Microwave Installation, Pathing and Alignment</li>
    <li>Fiber / Sweep / RET/ PIM Testing</li>
    <li>Small Cells</li>
    <li>Civil installation (concrete/steel platforms/electrical)</li>
  </ul>
  <div class="abs" style="left:651px;top:3036px;width:299px;height:309px;background:var(--green)"></div>
  <div class="abs" style="left:598px;top:3078px;width:299px;height:310px;background:linear-gradient(180deg,#efd59a 0%,#d9ac63 50%,#6b5330 80%,#15120d 100%)" role="img" aria-label="Photo of tower silhouettes with dish antennas against a golden sky"></div>
</section>

<!-- footer -->
<footer class="abs footer"></footer>
<div class="abs brand" style="left:250px;top:3500px;color:#fff;font-size:46px;line-height:52px;width:260px">Brannock<br>Spires</div>
<h2 class="abs serif sub-title">Subscribe To Newsletters</h2>
<div class="abs sub-lead">Lorem Ipsum has been the industry's standard dummy</div>
<div class="abs input">Email Address Your</div>
<div class="abs btn" style="left:845px;top:3566px;width:106px;height:35px;background:var(--green);font-size:9px">SUBSCRIBE</div>
<div class="abs hr" style="left:250px;top:3640px;width:701px"></div>

<h4 class="abs" style="left:252px;top:3671px;font-size:12.5px;color:#fff">Contact us</h4>
<div class="abs" style="left:252px;top:3710px;width:195px;font-size:9px;line-height:14px;color:#dbe6f3">
  Lorem Ipsum is simply dummy text of the printing and typesetting industry.
  <span style="display:block;margin-top:6px">Address : Pell Row Arden<br>48210, KR Q7M</span>
  Phone Number : 555 018 274<br>
  Email : info@brannockspires.com
</div>

<h4 class="abs" style="left:474px;top:3670px;font-size:12.5px;color:#fff">Quick Link</h4>
<ul class="abs quick" style="left:474px;top:3709px">
  <li>» Home</li><li>» About</li><li>» Services</li><li>» Contract</li><li>» Careers</li><li>» Gallery</li>
</ul>

<h4 class="abs" style="left:595px;top:3671px;font-size:12.5px;color:#fff">Recent post</h4>
<div class="abs" style="left:596px;top:3709px;width:185px;font-size:9px;line-height:14px;color:#dbe6f3">
  Lorem Ipsum is simply dummy text of the printing and typesetting industry.
  <span style="display:block;margin-top:6px">2 Hours ago</span>
  <span style="display:block;margin-top:18px">Lorem Ipsum is simply dummy text of the printing and typesetting industry.</span>
  <span style="display:block;margin-top:6px">2 Hours ago</span>
</div>

<h4 class="abs" style="left:809px;top:3671px;font-size:12.5px;color:#fff">Connect with us</h4>
<div class="abs social" style="left:810px;top:3708px"></div>
<div class="abs social" style="left:848px;top:3708px"></div>
<div class="abs social" style="left:886px;top:3708px"></div>
<div class="abs social" style="left:925px;top:3708px"></div>
<div class="abs social" style="left:810px;top:3750px"></div>
<div class="abs social" style="left:848px;top:3750px"></div>
<div class="abs social" style="left:886px;top:3750px"></div>
<div class="abs social" style="left:925px;top:3750px"></div>

<div class="abs hr" style="left:250px;top:3856px;width:701px"></div>
<div class="abs" style="left:0;width:1200px;top:3875px;text-align:center;font-size:9px;color:#dbe6f3">Copyright @ 2019 <b style="color:#fff">Brannock Spires</b> All Right Reserved</div>

</body>
</html>
```